Kestrel Motorworks Card

Our company is an offroad fabrication shop that does everything from product installs to complete turnkey offroad racers. We are looking to generate new business cards for the 2014 Lords of the Canyon race in February. This is one of the largest offroad races in the country. We would like to see designs that incorporate the colors used in our logo - black, red, and white.

Industry/Entity Type

Shop

Contact Information for Business Card

KESTREL Motorworks, 2873 Marwood Ln. Houston, TX, 713-452-3071, www.kestrelmotorworks.example, Leon Farrowby, Owen Tilsley, Owners.

Requirements
Nice to have
• Would like to see the Logo full size on the back size of the car.

```html
<!DOCTYPE html>
<html lang="en">
<head>
<meta charset="utf-8">
<title>Kestrel Motorworks Business Card</title>
<link rel="stylesheet" href="https://fonts.googleapis.com/css2?family=Orbitron:wght@700&family=Michroma&display=swap">
<style>
  :root {
    --page: #f4f4f4;
    --card: #050505;
    --red: #e31e24;
    --white: #ffffff;
    --grey: #8a8a8a;
    --gauge-dark: #141414;
  }
  html, body {
    margin: 0;
    padding: 0;
    width: 1200px;
    height: 900px;
    overflow: hidden;
    background: var(--page);
  }
  .canvas {
    position: relative;
    width: 1200px;
    height: 900px;
  }
  .card {
    position: absolute;
    width: 531px;
    height: 310px;
    background: var(--card);
    overflow: hidden;
  }
  .card-front { left: 54px; top: 130px; }
  .card-back { left: 619px; top: 128px; }

  .gauge-art {
    position: absolute;
    left: -40px;
    top: 130px;
    width: 330px;
    height: 330px;
    border-radius: 50%;
    background:
      radial-gradient(circle at 52% 28%, rgba(227,30,36,0.85) 0 12%, rgba(227,30,36,0) 40%),
      radial-gradient(circle at 45% 45%, #2a2a2a 0 35%, var(--gauge-dark) 60%, var(--card) 72%);
  }

  .owners {
    position: absolute;
    right: 26px;
    top: 22px;
    text-align: right;
    font-family: "Michroma", sans-serif;
    font-size: 12px;
    line-height: 17px;
    color: var(--white);
  }
  .owners .first { color: var(--red); }
  .owners .role { color: var(--grey); display: block; font-size: 11px; }

  .company {
    position: absolute;
    left: 252px;
    top: 134px;
    width: 260px;
    font-family: "Orbitron", sans-serif;
    font-weight: 700;
    font-size: 19px;
    color: var(--red);
    text-align: right;
    white-space: nowrap;
    padding-bottom: 6px;
    background: linear-gradient(to bottom, rgba(0,0,0,0) 55%, rgba(60,60,60,0.6) 85%, rgba(0,0,0,0) 100%);
  }
  .contact {
    position: absolute;
    left: 270px;
    top: 184px;
    width: 250px;
    text-align: center;
    font-family: "Michroma", sans-serif;
    color: var(--white);
    font-size: 12px;
    line-height: 18px;
  }
  .contact .web { color: var(--red); font-size: 10px; line-height: 14px; display: block; }

  .back-mark {
    position: absolute;
    inset: 0;
    display: flex;
    align-items: center;
    justify-content: center;
    gap: 18px;
  }
  .back-mark .square {
    width: 38px;
    height: 38px;
    background: var(--red);
  }
  .back-mark .name {
    font-family: "Orbitron", sans-serif;
    font-weight: 700;
    font-size: 34px;
    color: var(--red);
    white-space: nowrap;
  }
</style>
</head>
<body>
<div class="canvas">
  <section class="card card-front">
    <div class="gauge-art" role="img" aria-label="Speedometer dial with needle near 300 and red glow"></div>
    <p class="owners" style="margin:0">
      <span class="first">LEON</span> Farrowby, <span class="first">OWEN</span> Tilsley,
      <span class="role">Owners</span>
    </p>
    <div class="company">KESTREL Motorworks</div>
    <p class="contact" style="margin:0">
      2873 Marwood Ln. Houston, TX<br>
      713-452-3071<br>
      <span class="web">www.kestrelmotorworks.example</span>
    </p>
  </section>

  <section class="card card-back">
    <div class="back-mark">
      <span class="square"></span>
      <span class="name">KESTREL Motorworks</span>
    </div>
  </section>
</div>
</body>
</html>
```